Auto Detailing Facility Needs Facebook Cover Photo

Looking for a beautiful Facebook cover photo using our logo and a photo, including our business information. Does not have to use the photo provided but the logo must be in there. I want an eye-catching cover photo that promotes the luxury brand.

Website: www.glossbayauto.com
Phone: 508-555-0147
Address: 412 Lower Maple Rd Unit B-3 Harlow Point, VT 02091

Industry/Entity Type

Automotive

Colors

Designer to choose colors to be used in the design.

```html
<!DOCTYPE html>
<html lang="en">
<head>
<meta charset="utf-8">
<title>Gloss Bay Auto Care – Cover Variants</title>
<link rel="stylesheet" href="https://fonts.googleapis.com/css2?family=Barlow:wght@300;400;600;700&display=swap">
<style>
  :root {
    --board: #303030;
    --rule: #ffffff;
  }
  html, body {
    margin: 0;
    padding: 0;
    width: 1200px;
    height: 1200px;
    overflow: hidden;
    background: var(--board);
    font-family: "Barlow", Arial, sans-serif;
  }
  .board {
    position: relative;
    width: 1200px;
    height: 1200px;
  }
  .cover {
    position: absolute;
    left: 163px;
    width: 873px;
    height: 330px;
    background: var(--panel);
    color: var(--ink);
    overflow: hidden;
  }
  .cover--light { top: 55px;  --panel: #ffffff; --ink: #141414; }
  .cover--grey  { top: 434px; --panel: #4b4b4b; --ink: #ffffff; }
  .cover--dark  { top: 815px; --panel: #000000; --ink: #ffffff; }

  .cover__art {
    position: absolute;
    inset: 0;
    width: 873px;
    height: 330px;
  }
  .cover__band { fill: var(--panel); }
  .cover__rule { stroke: var(--rule); stroke-width: 2.6; }

  .brand-mark {
    position: absolute;
    left: 84px;
    top: 56px;
    font-size: 11px;
    font-weight: 400;
    letter-spacing: 1.5px;
    color: var(--ink);
  }
  .cover__title {
    position: absolute;
    left: 32px;
    top: 96px;
    margin: 0;
    font-size: 25px;
    font-weight: 700;
    line-height: 28px;
    letter-spacing: 0.3px;
  }
  .cover__tagline {
    position: absolute;
    left: 32px;
    top: 124px;
    margin: 0;
    font-size: 25px;
    font-weight: 300;
    line-height: 28px;
  }
  .contact {
    position: absolute;
    left: 32px;
    top: 196px;
    margin: 0;
    padding: 0;
    list-style: none;
    font-size: 9.5px;
    font-weight: 600;
    line-height: 13px;
  }
  .contact__item {
    display: flex;
    align-items: center;
    gap: 11px;
  }
  .contact__icon {
    width: 8px;
    height: 9px;
    fill: none;
    stroke: var(--ink);
    stroke-width: 1;
  }
</style>
</head>
<body>
<main class="board">

  <section class="cover cover--light">
    <svg class="cover__art" viewBox="0 0 873 330">
      <defs>
        <linearGradient id="photoTone" x1="0" y1="0" x2="0" y2="1">
          <stop offset="0" stop-color="#5d8a45"/>
          <stop offset="0.28" stop-color="#a9b07a"/>
          <stop offset="0.45" stop-color="#e6c31c"/>
          <stop offset="0.72" stop-color="#b89a12"/>
          <stop offset="1" stop-color="#2b2b2b"/>
        </linearGradient>
      </defs>
      <polygon role="img" aria-label="Photo of a yellow sports car parked beside trees" points="395,0 873,0 873,330 401,330 233,167" fill="url(#photoTone)"/>
      <polygon class="cover__band" points="629,0 761,0 873,112 873,245"/>
      <polygon class="cover__band" points="785,0 840,0 873,33 873,88"/>
      <line class="cover__rule" x1="430" y1="0" x2="225" y2="212"/>
      <line class="cover__rule" x1="466" y1="0" x2="256" y2="216"/>
      <line class="cover__rule" x1="245" y1="161" x2="419" y2="330"/>
    </svg>
    <div class="brand-mark">GLOSS BAY</div>
    <h1 class="cover__title">GLOSS BAY</h1>
    <p class="cover__tagline">auto care</p>
    <ul class="contact">
      <li class="contact__item"><svg class="contact__icon" viewBox="0 0 8 9"><rect x="1.5" y="0.5" width="5" height="8" rx="1"/></svg>508-555-0147</li>
      <li class="contact__item"><svg class="contact__icon" viewBox="0 0 8 9"><rect x="0.5" y="2" width="7" height="5"/><polyline points="0.5,2 4,5 7.5,2"/></svg>www.glossbayauto.com</li>
      <li class="contact__item"><svg class="contact__icon" viewBox="0 0 8 9"><path d="M4 8.5 C1.5 5.5 1 4.5 1 3.5 A3 3 0 0 1 7 3.5 C7 4.5 6.5 5.5 4 8.5Z"/><circle cx="4" cy="3.5" r="1"/></svg>412 Lower Maple Rd Unit B-3 Harlow Point, VT 02091</li>
    </ul>
  </section>

  <section class="cover cover--grey">
    <svg class="cover__art" viewBox="0 0 873 330">
      <polygon role="img" aria-label="Photo of a yellow sports car parked beside trees" points="395,0 873,0 873,330 401,330 233,167" fill="url(#photoTone)"/>
      <polygon class="cover__band" points="629,0 761,0 873,112 873,245"/>
      <polygon class="cover__band" points="785,0 840,0 873,33 873,88"/>
      <line class="cover__rule" x1="430" y1="0" x2="225" y2="212"/>
      <line class="cover__rule" x1="466" y1="0" x2="256" y2="216"/>
      <line class="cover__rule" x1="245" y1="161" x2="419" y2="330"/>
    </svg>
    <div class="brand-mark">GLOSS BAY</div>
    <h1 class="cover__title">GLOSS BAY</h1>
    <p class="cover__tagline">auto care</p>
    <ul class="contact">
      <li class="contact__item"><svg class="contact__icon" viewBox="0 0 8 9"><rect x="1.5" y="0.5" width="5" height="8" rx="1"/></svg>508-555-0147</li>
      <li class="contact__item"><svg class="contact__icon" viewBox="0 0 8 9"><rect x="0.5" y="2" width="7" height="5"/><polyline points="0.5,2 4,5 7.5,2"/></svg>www.glossbayauto.com</li>
      <li class="contact__item"><svg class="contact__icon" viewBox="0 0 8 9"><path d="M4 8.5 C1.5 5.5 1 4.5 1 3.5 A3 3 0 0 1 7 3.5 C7 4.5 6.5 5.5 4 8.5Z"/><circle cx="4" cy="3.5" r="1"/></svg>412 Lower Maple Rd Unit B-3 Harlow Point, VT 02091</li>
    </ul>
  </section>

  <section class="cover cover--dark">
    <svg class="cover__art" viewBox="0 0 873 330">
      <polygon role="img" aria-label="Photo of a yellow sports car parked beside trees" points="395,0 873,0 873,330 401,330 233,167" fill="url(#photoTone)"/>
      <polygon class="cover__band" points="629,0 761,0 873,112 873,245"/>
      <polygon class="cover__band" points="785,0 840,0 873,33 873,88"/>
      <line class="cover__rule" x1="430" y1="0" x2="225" y2="212"/>
      <line class="cover__rule" x1="466" y1="0" x2="256" y2="216"/>
      <line class="cover__rule" x1="245" y1="161" x2="419" y2="330"/>
    </svg>
    <div class="brand-mark">GLOSS BAY</div>
    <h1 class="cover__title">GLOSS BAY</h1>
    <p class="cover__tagline">auto care</p>
    <ul class="contact">
      <li class="contact__item"><svg class="contact__icon" viewBox="0 0 8 9"><rect x="1.5" y="0.5" width="5" height="8" rx="1"/></svg>508-555-0147</li>
      <li class="contact__item"><svg class="contact__icon" viewBox="0 0 8 9"><rect x="0.5" y="2" width="7" height="5"/><polyline points="0.5,2 4,5 7.5,2"/></svg>www.glossbayauto.com</li>
      <li class="contact__item"><svg class="contact__icon" viewBox="0 0 8 9"><path d="M4 8.5 C1.5 5.5 1 4.5 1 3.5 A3 3 0 0 1 7 3.5 C7 4.5 6.5 5.5 4 8.5Z"/><circle cx="4" cy="3.5" r="1"/></svg>412 Lower Maple Rd Unit B-3 Harlow Point, VT 02091</li>
    </ul>
  </section>

</main>
</body>
</html>
```